Company Profile to show details our company services, projects, products and locations

Required 20+ pages for the company profile.

I need company profile for our company, we are working in selling/rental diesel generators, the design should introduce the company services and project in a simple, attractive way.

Profile to be sent to customers and should give a brief about company details, projects, services, products and locations.

PLVM is a complete solution provider for diesel Generator industry supply, installation, testing, commissioning and maintenance with 10 years’ experience.

We are the soul dealer for KDW Volt Products ranging from (50 KVA up 220KVA) Powered by KDW engine and from (250 KVA to 25000KVA) powered by Brantley engine. KDW superior Generating sets are produced to the higher quality and are designed to meet UK & International quality standards.

Market competitors to PLVM: Velmora, NIVO, Zafin Energy....

Market Competitors for KDW: Brantley, ORV, HT Marlowe......

Target Market(s)

Companies in Oil & Gas, Construction, Utilities, Petrochemical......

Industry/Entity Type

Retail

Font styles to use
Sans Serif

Colors

Designer to choose colors to be used in the design.

Requirements
Must have
• Must show mainly that we sell diesel generators under a dealership from KDW and rental of diesel generators for QMT (Qasr Meridian Transmission) projects and private sector companies.
Nice to have
• Introduction about PLVM
• Details about KDW products (Diesel Generators & Light Towers)
• PLVM Projects
• Pictures
• Services
• Locations for, Showroom & workshop.
• Showroom:
• KDW - POWER SYSTEMS DIVISION
• Velo Strada Mall
• Tamarind Crest Road
• Ar Rimalah, Al Khobar 34870
• Workshop:
• PLVM – KDW POWER SYSTEMS DIVISION
• Warshat Halzun (Industrial Area)
• Al Masrif, Dharan
• Al Khobar 31487
• Kingdom of Saudi Arabia
• Tel : 00966-3-8475513
• Fax : 00966-3-8475720

```html
<!DOCTYPE html>
<html lang="en">
<head>
<meta charset="UTF-8">
<title>PLVM – Why We?</title>
<link rel="stylesheet" href="https://fonts.googleapis.com/css2?family=Lato:wght@300;400;700;900&family=Oswald:wght@600&display=swap">
<style>
  :root {
    --page: #ffffff;
    --slide-light: #e4e4e4;
    --slide-mid: #c9c9c9;
    --ink: #5a5a5a;
    --ink-strong: #4d4d4d;
    --white: #ffffff;
    --amber: #f5a623;
    --footer-ink: #2b2f3a;
  }
  * { margin: 0; padding: 0; box-sizing: border-box; }
  html, body { width: 1200px; height: 1000px; overflow: hidden; background: var(--page); }
  body { position: relative; font-family: "Lato", sans-serif; }

  .slide { position: absolute; left: 32px; top: 85px; width: 1136px; height: 830px; overflow: hidden;
    background: linear-gradient(180deg, var(--slide-light) 0%, var(--slide-mid) 100%); }
  .slide-shape { position: absolute; inset: 0; }

  .earth-band { position: absolute; left: 0; top: 198px; width: 1136px; height: 385px;
    background:
      radial-gradient(ellipse at 35% 75%, rgba(230,170,80,0.45) 0%, rgba(0,0,0,0) 35%),
      radial-gradient(ellipse at 80% 60%, rgba(220,160,70,0.45) 0%, rgba(0,0,0,0) 30%),
      linear-gradient(180deg, #1a2a44 0%, #5d6f86 22%, #34465f 45%, #1f2a3d 75%, #3a4352 100%); }

  .brand-name { position: absolute; left: 70px; top: 140px; font-weight: 900; font-size: 42px;
    letter-spacing: 1px; color: var(--ink-strong); line-height: 1; }

  .page-title { position: absolute; right: 82px; top: 140px; color: var(--white);
    font-weight: 300; font-size: 54px; letter-spacing: 2px; }

  .reasons-panel { position: absolute; left: 65px; top: 253px; width: 590px; height: 552px;
    background: rgba(255,255,255,0.78); }
  .reasons-count { position: absolute; left: 86px; top: 275px; font-weight: 900; font-size: 150px;
    letter-spacing: -8px; color: var(--ink-strong); line-height: 1;
    transform: scaleX(0.82); transform-origin: left top; }
  .reasons-heading { position: absolute; left: 247px; top: 288px; font-weight: 900; font-size: 70px;
    color: var(--ink-strong); line-height: 1; letter-spacing: -3px; }
  .reasons-sub { position: absolute; left: 248px; top: 360px; font-weight: 700; font-size: 24px;
    color: var(--ink); line-height: 31px; }
  .reasons-list { position: absolute; left: 243px; top: 447px; list-style: none; color: var(--ink);
    font-size: 26.5px; line-height: 31.7px; white-space: nowrap; }
  .reasons-list b { display: inline-block; min-width: 30px; font-weight: 700; }

  .uptime { position: absolute; left: 712px; top: 292px; width: 405px; color: var(--white); }
  .uptime-title { font-family: "Oswald", sans-serif; font-weight: 600; font-size: 30px;
    color: var(--amber); letter-spacing: 0.3px; margin: 0 0 10px 6px; line-height: 1.2; }
  .uptime-list { list-style: none; font-weight: 700; font-size: 19.5px; line-height: 21px; }
  .uptime-list li { position: relative; padding-left: 17px; margin-bottom: 41px; }
  .uptime-list li::before { content: ""; position: absolute; left: 2px; top: 6px; width: 9px; height: 9px;
    border-radius: 50%; background: var(--white); }

  .footer-rule { position: absolute; left: 60px; top: 852px; width: 518px; height: 1px; background: #7a7a7a; }
  .quote-author { position: absolute; left: 60px; top: 858px; font-size: 10px; line-height: 12px; color: var(--footer-ink); }
  .quote-text { position: absolute; left: 150px; top: 866px; font-weight: 700; font-size: 14px; color: var(--footer-ink); }
</style>
</head>
<body>
  <section class="slide">
    <svg class="slide-shape" width="1136" height="830" viewBox="0 0 1136 830" aria-hidden="true">
      <defs>
        <linearGradient id="slateFade" x1="0" y1="0" x2="1" y2="0.3">
          <stop offset="0" stop-color="#8a8a8a"/>
          <stop offset="0.35" stop-color="#4d4d4d"/>
          <stop offset="1" stop-color="#3d3d3d"/>
        </linearGradient>
      </defs>
      <polygon points="98,0 1136,0 1136,830 843,830" fill="url(#slateFade)"/>
    </svg>
    <div class="earth-band" role="img" aria-label="Photograph of Earth from orbit at night with city lights"></div>
    <svg class="slide-shape" width="1136" height="830" viewBox="0 0 1136 830" aria-hidden="true">
      <polygon points="620,583 1136,583 1136,830 843,830" fill="#444444"/>
    </svg>
  </section>

  <div class="brand-name">PLVM</div>
  <h1 class="page-title">WHY WE?</h1>

  <div class="reasons-panel"></div>
  <div class="reasons-count">10</div>
  <h2 class="reasons-heading">REASONS</h2>
  <p class="reasons-sub">TO BUY OUR GENERATORS<br>AND LIGHTNING TOWERS</p>
  <ol class="reasons-list">
    <li><b>1</b>EFFICIENT PERFORMANCE</li>
    <li><b>2</b>TOTAL CONTROL</li>
    <li><b>3</b>PLENTY IN THE TANK</li>
    <li><b>4</b>LOW OWNERSHIP COSTS</li>
    <li><b>5</b>ALL QUIET</li>
    <li><b>6</b>ULTIMATE PERFORMANCE</li>
    <li><b>7</b>EASY SERVICING</li>
    <li><b>8</b>MADE TO LAST</li>
    <li><b>9</b>COMPACT</li>
    <li><b>10</b> MANOEUVRABILITY</li>
  </ol>

  <div class="uptime">
    <h3 class="uptime-title">GENERATE UPTIME</h3>
    <ul class="uptime-list">
      <li>MONITOR &nbsp;OPERATIONAL HOURS AND FUEL LEVELS</li>
      <li>ENSURE PRODUCTIVITY</li>
      <li>THROUGH ALERTS &amp; NOTIFICATIONS</li>
      <li>ENSURE PRODUCTIVITY</li>
      <li>THROUGH ALERTS &amp; NOTIFICATIONSA LIFETIME OF KNOWLEDGE</li>
    </ul>
  </div>

  <div class="footer-rule"></div>
  <p class="quote-author">Samir Haddad<br>KDW Chairman</p>
  <p class="quote-text">“ALWAYS POWERING THE NEXT SHIFT”</p>
</body>
</html>
```